Breakfast Briefings / Lunch & Learn

I would like to have a double sided flyer size 8x10 to display the breakfast briefing on one side and Lunch & Learn on the other side.

Header on each side to say
2018 Calendar Breakfast Briefing (on the breakfast side)
2018 Calendar Lunch & Learn (on the lunch side)

I have attached a copy of the files we would like to use.

Industry/Entity Type

Learn

Colors

Designer to choose colors to be used in the design.

```html
<!DOCTYPE html>
<html lang="en">
<head>
<meta charset="utf-8">
<title>2018 Calendar – Breakfast Briefing / Lunch &amp; Learn</title>
<link href="https://fonts.googleapis.com/css2?family=Arvo:wght@700&family=Lora:ital,wght@1,400;1,700&family=Open+Sans:wght@600&display=swap" rel="stylesheet">
<style>
  :root{
    --blue:#1a82c0;
    --blue-deep:#1a74ad;
    --navy:#15507e;
    --sky:#c7ddf0;
    --paper:#ffffff;
    --backdrop:#b4b4b4;
  }
  *{box-sizing:border-box;margin:0;padding:0}
  html,body{width:1200px;height:897px;overflow:hidden}
  body{background:var(--backdrop);position:relative;font-family:'Arvo',serif}
  .page{position:absolute;background:var(--paper)}
  .page--breakfast{left:46px;top:106px;width:535px;height:670px}
  .page--lunch{left:623px;top:106px;width:539px;height:672px}

  /* breakfast side */
  .frame{position:absolute;left:17px;top:18px;width:502px;height:634px;border:3px solid var(--blue)}
  .hub{position:absolute;left:0;top:0;width:535px;height:670px}
  .title-box{position:absolute;border:2px solid var(--blue);padding:3px;background:var(--blue) content-box;color:#fff;font-weight:700;font-family:'Arvo',serif;display:flex;align-items:center}
  .title-box span{padding-left:20px;white-space:nowrap}
  .title-box--year{left:18px;top:24px;width:274px;height:40px;font-size:24px}
  .title-box--main{left:18px;top:70px;width:404px;height:62px;font-size:34px}

  .brand{position:absolute;font-family:'Arvo',serif;font-weight:700;font-size:20px;color:var(--blue);letter-spacing:1px;display:flex;align-items:center;gap:7px}
  .brand::before{content:"";width:14px;height:14px;background:var(--blue)}
  .page--breakfast .brand{left:30px;top:604px}
  .page--lunch .brand{left:31px;top:614px}

  .web-pill{position:absolute;height:32px;background:var(--blue);color:#fff;font-family:'Open Sans',sans-serif;font-weight:600;font-size:15px;display:flex;align-items:center;padding-left:46px}
  .page--breakfast .web-pill{left:278px;top:610px;width:241px}
  .page--lunch .web-pill{left:223px;top:609px;width:298px}
  .globe{position:absolute;left:-2px;top:-3px;width:38px;height:38px}

  /* lunch side */
  .topics{position:absolute;left:18px;top:17px;width:346px;height:567px;background:var(--blue-deep)}
  .topic{position:absolute;left:0;width:346px;height:50px}
  .topic__dome{position:absolute;left:20px;top:0;width:56px;height:28px}
  .topic__month{position:absolute;left:11px;top:27px;width:74px;height:19px;border-radius:10px;background:#fff;color:var(--navy);font-family:'Lora',serif;font-style:italic;font-size:12.5px;text-align:center;line-height:19px}
  .topic__title{position:absolute;left:99px;top:25px;width:245px;color:#fff;font-family:'Lora',serif;font-style:italic;font-weight:700;font-size:15.5px;line-height:20px}
  .topic__title--two{top:26px}

  .masthead{position:absolute;left:378px;top:17px;width:142px;height:226px;background:var(--sky);text-align:center;color:var(--blue-deep)}
  .masthead__hat{display:block;margin:10px auto 0;width:56px;height:52px}
  .masthead__title{font-family:'Arvo',serif;font-weight:700;font-size:27px;line-height:32px;margin-top:4px}
  .masthead__tag{font-family:'Arvo',serif;font-weight:700;font-size:12px;margin-top:4px}
  .tableware{position:absolute;left:378px;top:257px;width:142px;height:327px;background:linear-gradient(180deg,#1f87c6,#1a7ab4)}
  .footer-bar{position:absolute;left:18px;top:598px;width:503px;height:56px;border:2px solid var(--blue)}
</style>
</head>
<body>

<section class="page page--breakfast">
  <div class="frame"></div>

  <svg class="hub" viewBox="0 0 535 670">
    <defs>
      <linearGradient id="wood" x1="0" y1="0" x2="1" y2="1">
        <stop offset="0" stop-color="#a06a3d"/>
        <stop offset="1" stop-color="#6f4526"/>
      </linearGradient>
    </defs>
    <circle cx="266" cy="377" r="106" fill="none" stroke="#1a82c0" stroke-width="3" stroke-dasharray="10 6"/>
    <svg x="172" y="283" width="188" height="188" viewBox="0 0 188 188" role="img" aria-label="Photo of a tablet on a wooden desk showing the 2018 Breakfast Briefings calendar">
      <circle cx="94" cy="94" r="94" fill="url(#wood)"/>
    </svg>

    <g stroke="#1a82c0" stroke-width="1" stroke-dasharray="2 2" fill="none">
      <line x1="266" y1="252" x2="266" y2="222"/>
      <line x1="328.5" y1="268.8" x2="343.5" y2="242.8"/>
      <line x1="374" y1="314.5" x2="400" y2="299.5"/>
      <line x1="391" y1="377" x2="421" y2="377"/>
      <line x1="374" y1="439.5" x2="400" y2="454.5"/>
      <line x1="328.5" y1="485" x2="343.5" y2="511"/>
      <line x1="266" y1="502" x2="266" y2="532"/>
      <line x1="203.5" y1="485" x2="188.5" y2="511"/>
      <line x1="158" y1="439.5" x2="132" y2="454.5"/>
      <line x1="141" y1="377" x2="111" y2="377"/>
      <line x1="158" y1="314.5" x2="132" y2="299.5"/>
      <line x1="203.5" y1="269" x2="188.5" y2="243"/>
    </g>
    <g fill="#1a82c0">
      <circle cx="266" cy="252" r="2.5"/><circle cx="328.5" cy="268.8" r="2.5"/>
      <circle cx="374" cy="314.5" r="2.5"/><circle cx="391" cy="377" r="2.5"/>
      <circle cx="374" cy="439.5" r="2.5"/><circle cx="328.5" cy="485" r="2.5"/>
      <circle cx="266" cy="502" r="2.5"/><circle cx="203.5" cy="485" r="2.5"/>
      <circle cx="158" cy="439.5" r="2.5"/><circle cx="141" cy="377" r="2.5"/>
      <circle cx="158" cy="314.5" r="2.5"/><circle cx="203.5" cy="269" r="2.5"/>
    </g>

    <g class="dept-rings" fill="#fff" stroke="#1a82c0">
      <g transform="translate(266 185)"><circle r="35" stroke-width="1.2"/><circle r="30" stroke-width="1.6"/><path d="M-28 -24 A37 37 0 0 1 30 -22" fill="none" stroke-width="2.5"/></g>
      <g transform="translate(362 211)"><circle r="35" stroke-width="1.2"/><circle r="30" stroke-width="1.6"/><path d="M-28 -24 A37 37 0 0 1 30 -22" fill="none" stroke-width="2.5"/></g>
      <g transform="translate(432 281)"><circle r="35" stroke-width="1.2"/><circle r="30" stroke-width="1.6"/><path d="M-28 -24 A37 37 0 0 1 30 -22" fill="none" stroke-width="2.5"/></g>
      <g transform="translate(458 377)"><circle r="35" stroke-width="1.2"/><circle r="30" stroke-width="1.6"/><path d="M-28 -24 A37 37 0 0 1 30 -22" fill="none" stroke-width="2.5"/></g>
      <g transform="translate(432 473)"><circle r="35" stroke-width="1.2"/><circle r="30" stroke-width="1.6"/><path d="M-28 -24 A37 37 0 0 1 30 -22" fill="none" stroke-width="2.5"/></g>
      <g transform="translate(362 543)"><circle r="35" stroke-width="1.2"/><circle r="30" stroke-width="1.6"/><path d="M-28 -24 A37 37 0 0 1 30 -22" fill="none" stroke-width="2.5"/></g>
      <g transform="translate(266 569)"><circle r="35" stroke-width="1.2"/><circle r="30" stroke-width="1.6"/><path d="M-28 -24 A37 37 0 0 1 30 -22" fill="none" stroke-width="2.5"/></g>
      <g transform="translate(170 543)"><circle r="35" stroke-width="1.2"/><circle r="30" stroke-width="1.6"/><path d="M-28 -24 A37 37 0 0 1 30 -22" fill="none" stroke-width="2.5"/></g>
      <g transform="translate(100 473)"><circle r="35" stroke-width="1.2"/><circle r="30" stroke-width="1.6"/><path d="M-28 -24 A37 37 0 0 1 30 -22" fill="none" stroke-width="2.5"/></g>
      <g transform="translate(74 377)"><circle r="35" stroke-width="1.2"/><circle r="30" stroke-width="1.6"/><path d="M-28 -24 A37 37 0 0 1 30 -22" fill="none" stroke-width="2.5"/></g>
      <g transform="translate(100 281)"><circle r="35" stroke-width="1.2"/><circle r="30" stroke-width="1.6"/><path d="M-28 -24 A37 37 0 0 1 30 -22" fill="none" stroke-width="2.5"/></g>
      <g transform="translate(170 211)"><circle r="35" stroke-width="1.2"/><circle r="30" stroke-width="1.6"/><path d="M-28 -24 A37 37 0 0 1 30 -22" fill="none" stroke-width="2.5"/></g>
    </g>

    <g class="dept-labels" fill="#15507e" font-family="Arvo, serif" font-weight="700" font-size="5.6" text-anchor="middle">
      <text x="266" y="172"><tspan x="266">Medical</tspan><tspan x="266" dy="6.6">Owen</tspan><tspan x="266" dy="6.6">Park</tspan><tspan x="266" dy="6.6">2019</tspan><tspan x="266" dy="6.6">TBD</tspan></text>
      <text x="362" y="201"><tspan x="362">Sales</tspan><tspan x="362" dy="6.6">Lena Morris</tspan><tspan x="362" dy="6.6">2019</tspan><tspan x="362" dy="6.6">TBD</tspan></text>
      <text x="432" y="275"><tspan x="432">Finance</tspan><tspan x="432" dy="6.6">Tom Baker</tspan><tspan x="432" dy="6.6">March</tspan></text>
      <text x="458" y="368"><tspan x="458">R&amp;D</tspan><tspan x="458" dy="6.6">Sara</tspan><tspan x="458" dy="6.6">Lind</tspan><tspan x="458" dy="6.6">April</tspan></text>
      <text x="432" y="464"><tspan x="432">Operations</tspan><tspan x="432" dy="6.6">Hugo</tspan><tspan x="432" dy="6.6">Weiss</tspan><tspan x="432" dy="6.6">May</tspan></text>
      <text x="362" y="537"><tspan x="362">Clinical/ Reg</tspan><tspan x="362" dy="6.6">Ivy Chen</tspan><tspan x="362" dy="6.6">June</tspan></text>
      <text x="266" y="560"><tspan x="266">Quality</tspan><tspan x="266" dy="6.6">Martin</tspan><tspan x="266" dy="6.6">Vogel</tspan><tspan x="266" dy="6.6">July</tspan></text>
      <text x="170" y="534"><tspan x="170">People</tspan><tspan x="170" dy="6.6">Ruth</tspan><tspan x="170" dy="6.6">Evans</tspan><tspan x="170" dy="6.6">August</tspan></text>
      <text x="100" y="464"><tspan x="100">Marketing</tspan><tspan x="100" dy="6.6">Felix</tspan><tspan x="100" dy="6.6">Moreau</tspan><tspan x="100" dy="6.6">September</tspan></text>
      <text x="74" y="371"><tspan x="74">Legal</tspan><tspan x="74" dy="6.6">Nora Quinn</tspan><tspan x="74" dy="6.6">October</tspan></text>
      <text x="100" y="268"><tspan x="100">Market</tspan><tspan x="100" dy="6.6">Access</tspan><tspan x="100" dy="6.6">Paula</tspan><tspan x="100" dy="6.6">Ortega</tspan><tspan x="100" dy="6.6">November</tspan></text>
      <text x="170" y="205"><tspan x="170">TOS</tspan><tspan x="170" dy="6.6">Ben Walsh</tspan><tspan x="170" dy="6.6">December</tspan></text>
    </g>
  </svg>

  <h2 class="title-box title-box--year"><span>2018 Calendar</span></h2>
  <h1 class="title-box title-box--main"><span>Breakfast Briefing</span></h1>

  <div class="brand">veloro</div>
  <div class="web-pill">
    <svg class="globe" viewBox="0 0 38 38" aria-hidden="true">
      <circle cx="19" cy="19" r="18" fill="#fff" stroke="#1a82c0" stroke-width="2"/>
      <circle cx="19" cy="19" r="12" fill="#1a82c0"/>
      <g fill="none" stroke="#fff" stroke-width="1.1">
        <circle cx="19" cy="19" r="9"/><ellipse cx="19" cy="19" rx="4" ry="9"/>
        <line x1="10" y1="19" x2="28" y2="19"/><path d="M11.5 14h15M11.5 24h15"/>
      </g>
    </svg>
    www.companyname.com
  </div>
</section>

<section class="page page--lunch">
  <div class="topics">
    <svg width="0" height="0" style="position:absolute">
      <defs>
        <symbol id="dome" viewBox="0 0 56 28">
          <circle cx="28" cy="4" r="3" fill="#fff"/>
          <path d="M8 22 A20 17 0 0 1 48 22 Z" fill="#fff"/>
          <rect x="4" y="22" width="48" height="3" rx="1.5" fill="#fff"/>
          <path d="M16 13h22M14 18h26" stroke="#1a74ad" stroke-width="1.4"/>
        </symbol>
      </defs>
    </svg>
    <div class="topic" style="top:14px"><svg class="topic__dome"><use href="#dome"/></svg><div class="topic__month">March</div><div class="topic__title">Mindfulness</div></div>
    <div class="topic" style="top:68px"><svg class="topic__dome"><use href="#dome"/></svg><div class="topic__month">April</div><div class="topic__title">Nutrition and Lifestyle Coaching</div></div>
    <div class="topic" style="top:122px"><svg class="topic__dome"><use href="#dome"/></svg><div class="topic__month">May</div><div class="topic__title">What is Neuromodulation?</div></div>
    <div class="topic" style="top:178px"><svg class="topic__dome"><use href="#dome"/></svg><div class="topic__month">June</div><div class="topic__title">Achieve Your Goals</div></div>
    <div class="topic" style="top:232px"><svg class="topic__dome"><use href="#dome"/></svg><div class="topic__month">July</div><div class="topic__title topic__title--two">Changing Your LifePositive Thinking</div></div>
    <div class="topic" style="top:288px"><svg class="topic__dome"><use href="#dome"/></svg><div class="topic__month">August</div><div class="topic__title topic__title--two">Clean Eating How Do I Get Started</div></div>
    <div class="topic" style="top:343px"><svg class="topic__dome"><use href="#dome"/></svg><div class="topic__month">September</div><div class="topic__title">Budgeting 101 Financial Wellness</div></div>
    <div class="topic" style="top:402px"><svg class="topic__dome"><use href="#dome"/></svg><div class="topic__month">October</div><div class="topic__title">Busted! Nutrition Myths</div></div>
    <div class="topic" style="top:462px"><svg class="topic__dome"><use href="#dome"/></svg><div class="topic__month">November</div><div class="topic__title">Time Management</div></div>
    <div class="topic" style="top:518px"><svg class="topic__dome"><use href="#dome"/></svg><div class="topic__month">December</div><div class="topic__title">First Time Home Buyers</div></div>
  </div>

  <header class="masthead">
    <svg class="masthead__hat" viewBox="0 0 64 60" role="img" aria-label="Chef hat icon">
      <rect x="6" y="4" width="52" height="52" rx="14" fill="#1a74ad"/>
    </svg>
    <h1 class="masthead__title">2018<br>Calendar<br>Lunch &amp;<br>Learn</h1>
    <p class="masthead__tag">Life. Long.Learn</p>
  </header>

  <div class="tableware" role="img" aria-label="Illustration of a knife, fork, spoon and a steaming cup on a saucer"></div>

  <div class="footer-bar"></div>
  <div class="brand">veloro</div>
  <div class="web-pill">
    <svg class="globe" viewBox="0 0 38 38" aria-hidden="true">
      <circle cx="19" cy="19" r="18" fill="#fff" stroke="#1a82c0" stroke-width="2"/>
      <circle cx="19" cy="19" r="12" fill="#1a82c0"/>
      <g fill="none" stroke="#fff" stroke-width="1.1">
        <circle cx="19" cy="19" r="9"/><ellipse cx="19" cy="19" rx="4" ry="9"/>
        <line x1="10" y1="19" x2="28" y2="19"/><path d="M11.5 14h15M11.5 24h15"/>
      </g>
    </svg>
    www.companyname.com
  </div>
</section>

</body>
</html>
```